Life Coaching Business Card

Please check out my website at www.lorettavisbeck.com. Ideally I would like to use the same colors that I used on the site to match my business cards i.e: pink, green, teal, white
I want the final design to include a picture of me and also to be appealing and eye catching. For the picture I submitted, you can crop it smaller to just have my face (exclude my chest) showing.
Industry/Entity Type
Business
Contact Information for Business Card
Loretta Visbeck
Transformational Life Coach
web: www.lorettavisbeck.com
email: loretta@lorettavisbeck.com
Phone: 555-318-7042
Look and feel
Each slider illustrates characteristics of the customer's brand and the style your logo design should communicate.

```html
<!DOCTYPE html>
<html lang="en">
<head>
<meta charset="utf-8">
<title>Loretta Visbeck – Business Card</title>
<link rel="stylesheet" href="https://fonts.googleapis.com/css2?family=Russo+One&family=Jura:wght@300;400&display=swap">
<style>
  :root {
    --teal: #5cffe6;
    --white: #ffffff;
    --lime: #aaff00;
    --ink: #0d0d0d;
  }
  html, body {
    margin: 0;
    padding: 0;
    overflow: hidden;
    background: var(--white);
  }
  .card {
    position: relative;
    width: 1200px;
    height: 686px;
    overflow: hidden;
    background: var(--lime);
  }
  .band-top {
    position: absolute;
    left: 0; top: 0;
    width: 100%;
    height: 293px;
    background: var(--teal);
  }
  .band-name {
    position: absolute;
    left: 0; top: 293px;
    width: 100%;
    height: 88px;
    background: var(--white);
    display: flex;
    align-items: center;
    justify-content: center;
  }
  .name {
    margin: 0;
    font-family: "Russo One", sans-serif;
    font-weight: 400;
    font-size: 64px;
    font-variant: small-caps;
    letter-spacing: 2px;
    color: var(--ink);
    line-height: 1;
    padding-top: 6px;
  }
  .title {
    position: absolute;
    left: 0; top: 388px;
    width: 100%;
    margin: 0;
    text-align: center;
    font-family: "Jura", sans-serif;
    font-weight: 300;
    font-size: 50px;
    font-variant: small-caps;
    letter-spacing: 1px;
    color: var(--white);
    line-height: 1;
  }
</style>
</head>
<body>
  <div class="card">
    <div class="band-top"></div>
    <div class="band-name">
      <h1 class="name">Loretta Visbeck</h1>
    </div>
    <p class="title">Transformational Life Coach</p>
  </div>
</body>
</html>
```